Website For Ladder Company

I have a client that needs a new look to a stale website. Notes:

They like the the grays and reds of trelvaquip.com

i like the layout of this theme so i can get them a responsive design but it is a little too clean / white and needs some more color. I like this font and typography style http://fennimarklabs.com/

They like the layout of vurx.com but not black

Current site is halbrenner.com but I want to make sure you work directly through me and NOT CONTACT THE CLIENT DIRECTLY

There needs to be a blog feed section, place for featured video, intro paragraph and get all their current navigation.

there will be no flash on the site but a similar way they have the different types of ladder categories should be integrated

I envisioned this image in the header in some fashion http://www.plivorabank.com/cat.mhtml?searchterm=on+a+ladder&search_group=&lang=en&search_source=search_form#id=274519036&src=93k_4TRmpaQ8LdeYwnBzKv-7-41 with a tagline over it saying

Now Would Be a Good Time to Know What Ladder You Use. Trust Halbrenner.

Industry/Entity Type

Fashion

```html
<!DOCTYPE html>
<html lang="en">
<head>
<meta charset="utf-8">
<title>Halbrenner – Ladders</title>
<link href="https://fonts.googleapis.com/css2?family=Open+Sans:wght@400;600;700;800&display=swap" rel="stylesheet">
<style>
  :root{
    --red:#d0202a;
    --red-dark:#a9161f;
    --ink:#333;
    --muted:#777;
    --line:#dcdcdc;
    --panel:#f2f2f2;
    --band:#e9e9e9;
    --footer:#3a3a3a;
    --footer-dark:#2c2c2c;
    --white:#fff;
  }
  *{box-sizing:border-box;margin:0;padding:0}
  html,body{width:880px;height:1200px;overflow:hidden}
  body{font-family:"Open Sans",Arial,sans-serif;color:var(--ink);background:var(--white);font-size:11px;line-height:1.5}
  .wrap{width:820px;margin:0 auto;position:relative}

  /* header */
  .site-header{height:88px;border-bottom:3px solid var(--red);background:var(--white)}
  .site-header .wrap{height:100%}
  .brand{position:absolute;left:0;top:12px;font-weight:800;font-size:30px;color:var(--red);letter-spacing:-.5px}
  .search{position:absolute;right:0;top:16px;width:150px;height:22px;border:1px solid var(--line);border-radius:3px;display:flex;align-items:center;padding:0 6px;color:#999;font-size:10px;gap:6px}
  .main-nav{position:absolute;right:0;top:46px;display:flex;gap:0}
  .main-nav a{display:block;padding:10px 14px 14px;font-size:10.5px;font-weight:600;text-transform:uppercase;color:#555;text-decoration:none}
  .main-nav a.active{color:var(--red);border-bottom:3px solid var(--red)}

  /* hero */
  .hero{position:relative;height:382px;background:linear-gradient(100deg,#8a4a3a 0%,#9a5a48 34%,#c9d3dc 34%,#e8edf2 60%,#b9c4cf 100%)}
  .hero-photo{position:absolute;inset:0}
  .hero-caption{position:absolute;left:0;top:36px;width:470px;background:rgba(40,40,40,.72);color:var(--white);padding:14px 20px 16px 40px}
  .hero-caption h1{font-size:25px;font-weight:600;line-height:1.2;margin-bottom:8px}
  .hero-caption p{font-size:10.5px;line-height:1.55;color:#eee}
  .pager{height:22px;display:flex;justify-content:flex-end;align-items:center;gap:5px;padding-right:30px}
  .pager span{width:8px;height:8px;border-radius:50%;background:#c8c8c8}
  .pager span.on{background:var(--red)}

  /* intro */
  .intro{background:var(--band);height:230px;padding-top:18px}
  .intro .wrap{display:flex;gap:30px}
  .intro-text{flex:1}
  .intro-brand{font-weight:800;font-size:20px;color:var(--red);margin-bottom:6px;border-bottom:1px solid var(--line);padding-bottom:4px}
  .intro-text p{font-size:10px;color:#555;line-height:1.6}
  .more{display:block;text-align:right;font-size:10px;color:var(--red);margin-top:8px;font-weight:600}
  .video{width:240px;height:180px;border:4px solid var(--white);box-shadow:0 1px 3px rgba(0,0,0,.2);position:relative;background:linear-gradient(160deg,#d9e4ee,#9fb3c4 60%,#6e8295)}
  .video-bar{position:absolute;left:0;right:0;bottom:0;height:16px;background:rgba(0,0,0,.7)}
  .video svg{position:absolute;left:50%;top:50%;transform:translate(-50%,-50%)}

  /* blog */
  .blog-title{font-size:19px;font-weight:700;color:var(--red);margin:12px 0 8px}
  .blog-card{border:1px solid var(--line);background:var(--panel);height:200px;padding:12px 16px}
  .blog-meta{display:flex;gap:40px;font-size:9.5px;color:var(--muted);text-transform:uppercase;border-bottom:1px solid var(--line);padding-bottom:8px;margin-bottom:12px}
  .blog-meta span{display:flex;align-items:center;gap:6px}
  .blog-body{display:flex;gap:16px}
  .blog-thumb{width:150px;height:120px;flex:none;background:linear-gradient(170deg,#cfe0ee,#a8c0d4 55%,#7b8c7a)}
  .blog-body p{font-size:10px;color:#555;line-height:1.6;margin-bottom:6px}
  .read-more{float:right;background:var(--footer);color:var(--white);font-size:9.5px;font-weight:600;padding:4px 10px;border-radius:3px;margin-top:14px}

  /* categories carousel */
  .categories{display:flex;align-items:center;gap:10px;margin-top:12px;height:140px}
  .arrow{width:24px;height:46px;background:var(--footer);display:flex;align-items:center;justify-content:center;flex:none}
  .tiles{flex:1;display:flex;gap:12px}
  .tile{flex:1;height:128px;border:1px solid var(--line);background:var(--white);padding:6px}
  .tile div{width:100%;height:100%;background:linear-gradient(180deg,#f7f7f7,#ececec)}

  /* footer */
  .site-footer{position:absolute;left:0;right:0;top:1135px;height:65px;background:var(--footer);border-top:4px solid var(--footer-dark)}
  .site-footer .wrap{height:100%}
  .footer-brand{position:absolute;left:0;top:14px;font-weight:800;font-size:24px;color:var(--white)}
  .footer-links{position:absolute;right:0;top:16px;font-size:9.5px;color:#ccc;text-align:right;line-height:1.8}
</style>
</head>
<body>
  <header class="site-header">
    <div class="wrap">
      <div class="brand">Halbrenner</div>
      <div class="search">
        <svg width="10" height="10" viewBox="0 0 10 10"><circle cx="4" cy="4" r="3" fill="none" stroke="#999" stroke-width="1.3"/><line x1="6.3" y1="6.3" x2="9.3" y2="9.3" stroke="#999" stroke-width="1.3"/></svg>
        Search
      </div>
      <nav class="main-nav">
        <a class="active" href="#">Home</a>
        <a href="#">Features</a>
        <a href="#">Options</a>
        <a href="#">Replacement Parts</a>
        <a href="#">What's New</a>
        <a href="#">Trade Shows</a>
        <a href="#">Freight Carriers</a>
      </nav>
    </div>
  </header>

  <section class="hero">
    <div class="hero-photo" role="img" aria-label="Worker in a hard hat climbing a red extension ladder against a brick building"></div>
    <div class="hero-caption">
      <h1>Company was established in 1925</h1>
      <p>Halbrenner Company, headquartered in a small Midwest town, has been providing quality wood and metal ladders for more than ninety years. Our craftsmen build every ladder to order, ready for anything from retail stockrooms to industrial job sites.</p>
    </div>
  </section>
  <div class="pager"><span class="on"></span><span></span><span></span></div>

  <section class="intro">
    <div class="wrap">
      <div class="intro-text">
        <div class="intro-brand">Halbrenner</div>
        <p>Lorem ipsum dolor sit amet, consectetur adipiscing elit. Quisque dapibus accumsan orci, pretium eleifend arcu adipiscing eget. Fusce accumsan lacinia tincidunt. Phasellus rutrum enim auctor, vitae venenatis elit. Ut imperdiet hendrerit pulvinar. Cras et tellus a enim condimentum mollis at et tellus. Mauris dolor neque, elementum ac dictum eu, fermentum a nibh. Praesent id dui vitae venenatis elit. Ut imperdiet hendrerit pulvinar. Cras et tellus a enim condimentum mollis at et tellus. Mauris dolor neque, elementum ac dictum eu fermentum a nibh.</p>
        <a class="more" href="#">More Details »</a>
      </div>
      <div class="video" role="img" aria-label="Featured video still of a worker on a ladder">
        <svg width="44" height="44" viewBox="0 0 44 44"><circle cx="22" cy="22" r="21" fill="rgba(0,0,0,.55)"/><polygon points="17,13 32,22 17,31" fill="#fff"/></svg>
        <div class="video-bar"></div>
      </div>
    </div>
  </section>

  <main class="wrap">
    <h2 class="blog-title">Recent Blog Post</h2>
    <article class="blog-card">
      <div class="blog-meta">
        <span><svg width="9" height="9" viewBox="0 0 9 9"><rect x=".5" y="1.5" width="8" height="7" fill="none" stroke="#999"/></svg>April 26, 2013</span>
        <span><svg width="9" height="9" viewBox="0 0 9 9"><circle cx="4.5" cy="3" r="2" fill="#999"/><rect x="1" y="6" width="7" height="3" fill="#999"/></svg>Admin</span>
        <span><svg width="9" height="9" viewBox="0 0 9 9"><rect x=".5" y=".5" width="8" height="6" fill="none" stroke="#999"/></svg>6 Comments</span>
      </div>
      <div class="blog-body">
        <div class="blog-thumb" role="img" aria-label="Blog photo of a worker on a ladder outdoors"></div>
        <div>
          <p>Welcome! Have a look around but be patient while our new website is still under construction. We'll have a full launch soon. In the meantime, please subscribe to one of our social media pages to stay up to date on new ladders.</p>
          <p>Praesent eleifend arcu adipiscing eget. Fusce accumsan lacinia tincidunt. Phasellus tempor enim purus, vitae venenatis elit. Cras et tellus, notified when the site is finished.</p>
          <span class="read-more">Read more »</span>
        </div>
      </div>
    </article>

    <section class="categories">
      <div class="arrow"><svg width="10" height="14" viewBox="0 0 10 14"><polygon points="8,1 2,7 8,13" fill="#fff"/></svg></div>
      <div class="tiles">
        <div class="tile"><div role="img" aria-label="Red rolling work platform ladder"></div></div>
        <div class="tile"><div role="img" aria-label="Blue rolling stair ladder"></div></div>
        <div class="tile"><div role="img" aria-label="Blue steel rolling ladder"></div></div>
        <div class="tile"><div role="img" aria-label="Red warehouse ladder"></div></div>
        <div class="tile"><div role="img" aria-label="Yellow fiberglass step ladder"></div></div>
        <div class="tile"><div role="img" aria-label="Red rolling safety ladder"></div></div>
      </div>
      <div class="arrow"><svg width="10" height="14" viewBox="0 0 10 14"><polygon points="2,1 8,7 2,13" fill="#fff"/></svg></div>
    </section>
  </main>

  <footer class="site-footer">
    <div class="wrap">
      <div class="footer-brand">Halbrenner</div>
      <div class="footer-links">
        Home • Features • Options • What's New • Trade Shows • Contact Us<br>
        Halbrenner. Copyright © 2013. Privacy Policy
      </div>
    </div>
  </footer>
</body>
</html>
```